custom carpentry, woodworking and home repair company needs logo design and business card design

Attention: I apologize but I just received notification from my state that I cannot use the company name that I originally submitted (Beyond The Bench). The new name will be Joinolux We need a company logo and business card design for our new company based in the Hampton Roads area of Virginia. The company name is Joinolux. The final design should give a first impression of true craftsmanship and attention to detail. We would like the card to include the company name, my name Mark Tellman (owner), phone number (757) 348-2615, website (joinolux-example.com) and email address (mark@joinolux-example.com). Everything else is up to your discretion. Thanks, have fun, and good luck.

Industry/Entity Type

Business

Contact Information for Business Card

See project description

Logo Text

see project description

Colors

Designer to choose colors to be used in the design.

```html
<!DOCTYPE html>
<html lang="en">
<head>
<meta charset="utf-8">
<title>Joinolux Business Card</title>
<link rel="stylesheet" href="https://fonts.googleapis.com/css2?family=Lato:wght@400;700;900&display=swap">
<style>
  :root {
    --navy: #30435a;
    --white: #ffffff;
    --backdrop: #e9e7e3;
    --steel-light: #d6d6d6;
    --steel-dark: #8c8c8c;
  }
  * { margin: 0; padding: 0; box-sizing: border-box; }
  html, body {
    width: 1200px; height: 902px; overflow: hidden;
    background: var(--backdrop);
    font-family: "Lato", Arial, sans-serif;
  }
  .business-card {
    position: absolute; left: 100px; top: 166px;
    width: 1000px; height: 570px;
    background: var(--white);
    border-radius: 22px; overflow: hidden;
    box-shadow: 0 10px 30px rgba(0,0,0,0.15);
  }
  .card-shapes { position: absolute; inset: 0; }
  .contact-side { position: absolute; left: 66px; top: 0; color: var(--white); }
  .owner-name {
    position: absolute; top: 104px; left: 4px; white-space: nowrap;
    font-weight: 700; font-size: 34px; letter-spacing: 0.2px;
  }
  .owner-role {
    position: absolute; top: 139px; left: 0; font-size: 23px; font-weight: 400;
  }
  .mailing-address {
    position: absolute; top: 236px; left: 0; width: 400px;
    font-size: 24px; line-height: 33px; white-space: nowrap;
  }
  .contact-list {
    position: absolute; top: 368px; left: 0; list-style: none;
  }
  .contact-list li {
    display: flex; align-items: center; height: 34px;
    font-size: 24px; white-space: nowrap;
  }
  .contact-icon { width: 30px; height: 30px; margin-right: 9px; flex: none; }
  .brand {
    position: absolute; left: 600px; top: 250px; width: 320px;
    display: flex; align-items: center; justify-content: center; gap: 14px;
  }
  .brand-dot {
    width: 22px; height: 22px; border-radius: 50%; background: var(--navy);
  }
  .brand-name {
    font-family: "Lato", Arial, sans-serif;
    font-weight: 900; font-size: 56px; letter-spacing: 3px;
    color: var(--navy); text-transform: uppercase;
  }
</style>
</head>
<body>
  <div class="business-card">
    <svg class="card-shapes" width="1000" height="570" viewBox="0 0 1000 570" aria-hidden="true">
      <defs>
        <linearGradient id="steel" x1="0" y1="0" x2="0" y2="1">
          <stop offset="0" stop-color="var(--steel-light)"/>
          <stop offset="0.5" stop-color="var(--steel-dark)"/>
          <stop offset="1" stop-color="var(--steel-light)"/>
        </linearGradient>
      </defs>
      <path d="M0,0 H516 Q410,285 516,570 H0 Z" fill="var(--navy)"/>
      <path d="M528,0 Q432,285 528,570 Q448,285 528,0 Z" fill="url(#steel)"/>
    </svg>

    <div class="contact-side">
      <h1 class="owner-name">Mark Tellman</h1>
      <p class="owner-role">Owner</p>
      <address class="mailing-address" style="font-style:normal">
        PO BOX 111 your address,<br>2nd Street,3rd Lane<br>USA
      </address>
      <ul class="contact-list">
        <li>
          <svg class="contact-icon" viewBox="0 0 30 30" aria-hidden="true">
            <circle cx="15" cy="15" r="13.5" fill="none" stroke="#fff" stroke-width="2"/>
            <path d="M8.5,12 Q15,7 21.5,12 L20,14 L17.5,13 L17.5,11.5 Q15,10.8 12.5,11.5 L12.5,13 L10,14 Z M10.5,15.5 H19.5 L21,21 H9 Z" fill="#fff"/>
          </svg>
          (757) 348-2615
        </li>
        <li>
          <svg class="contact-icon" viewBox="0 0 30 30" aria-hidden="true">
            <circle cx="15" cy="15" r="13.5" fill="none" stroke="#fff" stroke-width="2"/>
            <rect x="8" y="10" width="14" height="10" fill="#fff"/>
            <path d="M8,10 L15,16 L22,10" fill="none" stroke="var(--navy)" stroke-width="1.5"/>
          </svg>
          mark@joinolux-example.com
        </li>
        <li>
          <svg class="contact-icon" viewBox="0 0 30 30" aria-hidden="true">
            <circle cx="15" cy="15" r="13.5" fill="none" stroke="#fff" stroke-width="2"/>
            <circle cx="15" cy="15" r="8" fill="none" stroke="#fff" stroke-width="1.5"/>
            <ellipse cx="15" cy="15" rx="3.5" ry="8" fill="none" stroke="#fff" stroke-width="1.3"/>
            <path d="M7,15 H23 M8.5,11 H21.5 M8.5,19 H21.5" stroke="#fff" stroke-width="1.2"/>
          </svg>
          joinolux-example.com
        </li>
      </ul>
    </div>

    <div class="brand">
      <span class="brand-dot" aria-hidden="true"></span>
      <span class="brand-name">Joinolux</span>
    </div>
  </div>
</body>
</html>
```